We need a business card design for a Dubai based company .

We need a business card for a Dubai based company called "Zernova Shisha & Charcoal Supply Co.". We mainly import Flavoured Tobacco products and Charcoal which is used for smoking in a Hookah/Shisha and distribute to the wholesalers and retailers. Logo file is attached herewith.

```html
<!DOCTYPE html>
<html lang="en">
<head>
<meta charset="utf-8">
<title>Zernova – Red Foil Business Card Options</title>
<link href="https://fonts.googleapis.com/css2?family=Arimo:ital,wght@1,400;1,700&family=Josefin+Sans:wght@400&family=Oswald:wght@300&display=swap" rel="stylesheet">
<style>
  :root {
    --page: #ffffff;
    --card: #f4f4f3;
    --card-edge: #dcdcdc;
    --foil-red: #c4282c;
    --accent-orange: #e0844f;
    --ink: #1c1c1c;
    --muted: #4a4a4a;
    --label: #111111;
  }
  * { margin: 0; padding: 0; box-sizing: border-box; }
  html, body { width: 1200px; height: 825px; overflow: hidden; background: var(--page); }
  .board { position: relative; width: 1200px; height: 825px; }

  .board-title, .option-title, .note {
    position: absolute;
    font-family: "Arimo", Arial, sans-serif;
    font-style: italic;
    font-weight: 700;
    color: var(--label);
  }
  .board-title { left: 420px; top: 10px; font-size: 19px; }
  .option-title { top: 48px; font-size: 19px; }
  .option-title.one { left: 149px; }
  .option-title.two { left: 707px; }

  .note { font-size: 15px; line-height: 19.5px; }
  .note .note-head { display: block; }
  .note .note-body { font-weight: 400; display: block; }
  .note-1a { left: 377px; top: 104px; }
  .note-1b { left: 377px; top: 304px; }
  .note-2a { left: 932px; top: 113px; }
  .note-2b { left: 932px; top: 313px; }

  .card {
    position: absolute;
    width: 304px;
    height: 174px;
    background: var(--card);
    border: 1px solid var(--card-edge);
  }
  .opt1 { left: 45px; }
  .opt2 { left: 580px; }
  .side-a { top: 103px; }
  .opt1.side-b { top: 300px; }
  .opt2.side-b { top: 305px; }

  .brand-name {
    font-family: "Josefin Sans", "Century Gothic", sans-serif;
    font-weight: 400;
    letter-spacing: 0.12em;
    text-transform: uppercase;
  }
  .brand-sub {
    font-family: "Josefin Sans", "Century Gothic", sans-serif;
    font-weight: 400;
    letter-spacing: 0.22em;
    text-transform: uppercase;
  }

  /* Side A – option 1: name in red foil */
  .foil-lockup {
    position: absolute; left: 0; right: 0; top: 66px;
    text-align: center; color: var(--foil-red);
  }
  .foil-lockup .brand-name { font-size: 34px; line-height: 36px; }
  .foil-lockup .brand-sub { font-size: 7px; margin-top: 6px; }

  /* Side A – option 2: minimal foil */
  .foil-minimal {
    position: absolute; left: 0; right: 0; top: 76px;
    display: flex; align-items: center; justify-content: center; gap: 10px;
    color: var(--foil-red);
  }
  .foil-minimal .mark-square {
    width: 16px; height: 16px; border: 2px solid var(--foil-red);
  }
  .foil-minimal .brand-name { font-size: 20px; line-height: 20px; padding-top: 3px; }

  /* Side B – shared */
  .back-lockup {
    position: absolute; left: 18px; top: 72px; width: 156px;
    text-align: center;
  }
  .back-lockup .brand-name { font-size: 21px; color: var(--ink); line-height: 22px; }
  .back-lockup .brand-sub { font-size: 4.8px; color: var(--foil-red); margin-top: 4px; letter-spacing: 0.2em; }

  .contact-list {
    position: absolute; left: 192px; top: 42px;
    list-style: none;
    font-family: "Oswald", "Arial Narrow", sans-serif;
    font-weight: 300;
    font-size: 7.5px;
    color: var(--muted);
  }
  .contact-list li { height: 19.3px; padding-top: 3px; position: relative; white-space: nowrap; }
  .contact-list li:not(:last-child)::after {
    content: ""; position: absolute; left: 0; bottom: 2px;
    width: 56px; height: 1px; background: var(--accent-orange);
  }
  .contact-list .email { text-transform: none; }
</style>
</head>
<body>
<main class="board">
  <h1 class="board-title">RED FOIL CARD</h1>
  <h2 class="option-title one">OPTION 1</h2>
  <h2 class="option-title two">OPTION 2</h2>

  <section class="card opt1 side-a" aria-label="Option 1 front">
    <div class="foil-lockup">
      <div class="brand-name">Zernova</div>
      <div class="brand-sub">Shisha &amp; Charcoal Supply Co.</div>
    </div>
  </section>
  <section class="card opt1 side-b" aria-label="Option 1 back">
    <div class="back-lockup">
      <div class="brand-name">Zernova</div>
      <div class="brand-sub">Shisha &amp; Charcoal Supply Co.</div>
    </div>
    <ul class="contact-list">
      <li>240 HARBOR LANE</li>
      <li>ELLMONT, MI 48710</li>
      <li>TEL: +00412098765</li>
      <li>WWW.ZERNOVA.COM</li>
      <li class="email">email: hello@zernova.co</li>
    </ul>
  </section>

  <p class="note note-1a">
    <span class="note-head">SIDE A</span>
    <span class="note-body">On this card the<br>Logo is printed in<br>Red Foil on side A</span>
  </p>
  <p class="note note-1b"><span class="note-head">SIDE B</span></p>

  <section class="card opt2 side-a" aria-label="Option 2 front">
    <div class="foil-minimal">
      <span class="mark-square"></span>
      <span class="brand-name">Zernova</span>
    </div>
  </section>
  <section class="card opt2 side-b" aria-label="Option 2 back">
    <div class="back-lockup">
      <div class="brand-name">Zernova</div>
      <div class="brand-sub">Shisha &amp; Charcoal Supply Co.</div>
    </div>
    <ul class="contact-list">
      <li>240 HARBOR LANE</li>
      <li>ELLMONT, MI 48710</li>
      <li>TEL: +00412098765</li>
      <li>WWW.ZERNOVA.COM</li>
      <li class="email">email: hello@zernova.co</li>
    </ul>
  </section>

  <p class="note note-2a">
    <span class="note-head">SIDE A</span>
    <span class="note-body">On this card the lines<br>are printed in<br>Red Foil on side A<br>A more minimal and<br>modern approach design<br>since the lines are a very<br>strong element and easy to rember</span>
  </p>
  <p class="note note-2b"><span class="note-head">SIDE B</span></p>
</main>
</body>
</html>
```